Business Card Design

We need a business card design for a Executive search firm based in London & the North East called Kestrelby. We specialise in mid - snr level (£50k - £200k) IT placements. Our company colour is navy blue.

Target Market(s)

CEO, HR Director, Sales Director/VP - (35 - 50), well educated, British, European & American

Industry/Entity Type

Business

Contact Information for Business Card

Kestrelby Staffing Limited, Owen Caskell
Mobile - 0044 7731 482 616
London Office - Kestrelby House, 27 Fernmoor, Wexcombe. HA5 3LQ
Tel: 00 44 20 418 62093
North East Office – Velmora Centre, Ashgrove Way, Tillerby, NE41 2RD
Tel: 00 44 191 6842051
www.kestrelbystaffing-example.com

Also the same details for my Business Partner Ravi Tolani
with his mobile number as 0044 7852 307718

Requirements
Must have
• must have the same logo

the logo needs to be the same but made sharper

```html
<!DOCTYPE html>
<html lang="en">
<head>
<meta charset="utf-8">
<title>Kestrelby Staffing – Business Cards</title>
<link href="https://fonts.googleapis.com/css2?family=Noto+Sans:wght@400;500&display=swap" rel="stylesheet">
<style>
  :root {
    --backdrop: #2b1c14;
    --white: #ffffff;
    --navy: #0d3a85;
    --navy-deep: #0b3279;
    --mid-blue: #2f70bb;
    --strip-blue: #3a7cc6;
    --ink: #123c8c;
    --logo-navy: #163f86;
  }
  * { margin: 0; padding: 0; box-sizing: border-box; }
  html, body { width: 1200px; height: 900px; overflow: hidden; }
  body {
    background: var(--backdrop);
    font-family: "Noto Sans", Arial, sans-serif;
    position: relative;
  }
  .card {
    position: absolute;
    width: 477px;
    height: 280px;
    background: var(--white);
    overflow: hidden;
  }
  .card--front-a { left: 58px;  top: 105px; }
  .card--front-b { left: 655px; top: 108px; }
  .card--back-a  { left: 58px;  top: 530px; }
  .card--back-b  { left: 655px; top: 530px; }

  /* Front */
  .contact-list { position: absolute; left: 14px; top: 20px; list-style: none; }
  .contact-item {
    display: flex; align-items: flex-start; gap: 8px;
    color: var(--ink); font-size: 11px; line-height: 13px;
    margin-bottom: 16px;
  }
  .contact-item--address { margin-bottom: 6px; }
  .contact-item svg { flex: 0 0 14px; width: 14px; height: 14px; fill: var(--ink); }
  .front-strip { position: absolute; left: 0; top: 178px; width: 100%; height: 10px; background: var(--strip-blue); }
  .front-band {
    position: absolute; left: 0; top: 188px; width: 100%; height: 92px;
    background: var(--navy); color: var(--white); padding: 14px 0 0 14px;
  }
  .person-name { font-size: 28px; font-weight: 400; letter-spacing: .5px; line-height: 34px; }
  .company-name { font-size: 17px; font-weight: 400; line-height: 22px; margin-top: 2px; }

  .logo {
    position: absolute; display: flex; align-items: center; gap: 8px;
    color: var(--logo-navy); font-size: 30px; font-weight: 400;
  }
  .card--front-a .logo, .card--front-b .logo { right: 22px; top: 78px; }
  .logo-dot { width: 16px; height: 16px; border-radius: 50%; background: var(--mid-blue); }

  /* Back */
  .back-top { position: absolute; left: 0; top: 0; width: 100%; height: 28px; background: var(--navy); }
  .back-logo-area { position: absolute; left: 0; top: 28px; width: 100%; height: 127px; display: flex; align-items: center; justify-content: center; }
  .back-logo-area .logo { position: static; font-size: 34px; }
  .back-divider { position: absolute; left: 0; top: 155px; width: 100%; height: 23px; background: var(--navy-deep); }
  .back-band {
    position: absolute; left: 0; top: 178px; width: 100%; height: 102px;
    background: var(--mid-blue); color: var(--white);
    display: flex; align-items: center; justify-content: center;
    font-size: 27px; font-weight: 500; letter-spacing: .3px;
  }
</style>
</head>
<body>

<svg width="0" height="0" style="position:absolute" aria-hidden="true">
  <defs>
    <symbol id="icon-phone" viewBox="0 0 24 24"><path d="M6.6 10.8a15.1 15.1 0 0 0 6.6 6.6l2.2-2.2c.3-.3.7-.4 1-.2 1.1.4 2.3.6 3.6.6.6 0 1 .4 1 1V20c0 .6-.4 1-1 1A17 17 0 0 1 3 4c0-.6.4-1 1-1h3.5c.6 0 1 .4 1 1 0 1.3.2 2.5.6 3.6.1.3 0 .7-.2 1z"/></symbol>
    <symbol id="icon-mobile" viewBox="0 0 24 24"><path d="M7 1h10a2 2 0 0 1 2 2v18a2 2 0 0 1-2 2H7a2 2 0 0 1-2-2V3a2 2 0 0 1 2-2zm0 3v14h10V4zm5 15.2a1.1 1.1 0 1 0 0 2.2 1.1 1.1 0 0 0 0-2.2z"/></symbol>
    <symbol id="icon-globe" viewBox="0 0 24 24"><path d="M12 2a10 10 0 1 0 0 20 10 10 0 0 0 0-20zm6.9 6h-2.9a15.7 15.7 0 0 0-1.4-3.6A8 8 0 0 1 18.9 8zM12 4c.8 1.2 1.5 2.5 1.9 4h-3.8c.4-1.4 1.1-2.8 1.9-4zM4.3 14a8.2 8.2 0 0 1 0-4h3.4a16.5 16.5 0 0 0 0 4zm.8 2h3a15.7 15.7 0 0 0 1.3 3.6A8 8 0 0 1 5.1 16zm3-8h-3a8 8 0 0 1 4.3-3.6C8.8 5.5 8.4 6.7 8.1 8zM12 20c-.8-1.2-1.5-2.5-1.9-4h3.8c-.4 1.4-1.1 2.8-1.9 4zm2.3-6H9.7a14.7 14.7 0 0 1 0-4h4.6a14.7 14.7 0 0 1 0 4zm.3 5.6c.6-1.1 1.1-2.3 1.4-3.6h2.9a8 8 0 0 1-4.3 3.6zm1.7-5.6a16.5 16.5 0 0 0 0-4h3.4a8.2 8.2 0 0 1 0 4z"/></symbol>
    <symbol id="icon-pin" viewBox="0 0 24 24"><path d="M12 2a7 7 0 0 0-7 7c0 5.2 7 13 7 13s7-7.8 7-13a7 7 0 0 0-7-7zm0 9.5a2.5 2.5 0 1 1 0-5 2.5 2.5 0 0 1 0 5z"/></symbol>
  </defs>
</svg>

<section class="card card--front-a" aria-label="Front of card, Ravi Tolani">
  <ul class="contact-list">
    <li class="contact-item"><svg><use href="#icon-phone"/></svg><span>00441916842051&nbsp; [Tillerby Office]</span></li>
    <li class="contact-item"><svg><use href="#icon-mobile"/></svg><span>00447852307718</span></li>
    <li class="contact-item"><svg><use href="#icon-globe"/></svg><span>www.kestrelbystaffing-example.com</span></li>
    <li class="contact-item contact-item--address"><svg><use href="#icon-pin"/></svg><span>London Office–Kestrelby House, 27<br>Fernmoor, Wexcombe. HA5 3LQ</span></li>
    <li class="contact-item contact-item--address"><svg><use href="#icon-pin"/></svg><span>North East Office – Velmora Centre<br>Ashgrove Way, Tillerby, NE41 2RD</span></li>
  </ul>
  <div class="logo"><span>Kestrelby</span><span class="logo-dot"></span></div>
  <div class="front-strip"></div>
  <div class="front-band">
    <p class="person-name">Ravi Tolani</p>
    <p class="company-name">Kestrelby Staffing Limited</p>
  </div>
</section>

<section class="card card--front-b" aria-label="Front of card, Owen Caskell">
  <ul class="contact-list">
    <li class="contact-item"><svg><use href="#icon-phone"/></svg><span>00442041862093&nbsp; [London Office]</span></li>
    <li class="contact-item"><svg><use href="#icon-mobile"/></svg><span>00447731482616</span></li>
    <li class="contact-item"><svg><use href="#icon-globe"/></svg><span>www.kestrelbystaffing-example.com</span></li>
    <li class="contact-item contact-item--address"><svg><use href="#icon-pin"/></svg><span>London Office–Kestrelby House, 27<br>Fernmoor, Wexcombe. HA5 3LQ</span></li>
    <li class="contact-item contact-item--address"><svg><use href="#icon-pin"/></svg><span>North East Office – Velmora Centre<br>Ashgrove Way, Tillerby, NE41 2RD</span></li>
  </ul>
  <div class="logo"><span>Kestrelby</span><span class="logo-dot"></span></div>
  <div class="front-strip"></div>
  <div class="front-band">
    <p class="person-name">Owen Caskell</p>
    <p class="company-name">Kestrelby Staffing Limited</p>
  </div>
</section>

<section class="card card--back-a" aria-label="Back of card">
  <div class="back-top"></div>
  <div class="back-logo-area"><div class="logo"><span>Kestrelby</span><span class="logo-dot"></span></div></div>
  <div class="back-divider"></div>
  <div class="back-band">Kestrelby Staffing Limited</div>
</section>

<section class="card card--back-b" aria-label="Back of card">
  <div class="back-top"></div>
  <div class="back-logo-area"><div class="logo"><span>Kestrelby</span><span class="logo-dot"></span></div></div>
  <div class="back-divider"></div>
  <div class="back-band">Kestrelby Staffing Limited</div>
</section>

</body>
</html>
```